Blue Harbor Car Finance Home Page

We need a desktop version mock up (we will base our mobile version off of this) of a website homepage for our auto loan business, Blue Harbor Car Finance. This does not need to be a functioning site, just a home page mock up. We are based in the metro St. Louis, MO area. We offer "guaranteed" auto loans for all credit types. We specialize in financing for bad/no credit customers. We are able to help rebuild these type of customers' credit, all while putting them in a great late model vehicle they'll love. Our online credit app takes less than 60 seconds, doesn't require a SS# and gives a free credit score if they fill it out within 3 minutes. We are looking for an outside perspective to help us in this design process. We are not completely sure what we want, but we do want it to be professional and secure looking, all while being unique and aesthetically pleasing. We want the customer to be able to put in their zip code to be directed to the right location that can get them pre approved. I attached a wireframe with some stuff we'd like to include, but in no way does it have to be in the same layout or the same ideas. We want everyone to "go crazy" with their creative side on this. Our current site is awful, here is a link to get a better idea: www.blueharborcarfinance-example.com. Attached is our logo too, base colors off of it. Watch our video that is also attached for a better idea.

Target Market(s)

Residents of the St. Louis Missouri Metro Area that need an auto loan. 24-55 Male and Female - Lots of "urban market" customers.

Industry/Entity Type

Loan

Number of Pages Required

1 page

Colors
9bcb3b

Requirements
Must have
• An area where the customer can enter their zip code - Be creative!
Nice to have
• See wireframe attachment for ideas - Be creative!

```html
<!DOCTYPE html>
<html lang="en">
<head>
<meta charset="utf-8">
<title>Blue Harbor Car Finance – Home</title>
<link rel="stylesheet" href="https://fonts.googleapis.com/css2?family=Figtree:wght@400;500;600;700&display=swap">
<style>
:root{
  --brand:#9bcb3b;
  --brand-dark:#86b22c;
  --accent-yellow:#e9e43c;
  --ink:#333333;
  --muted:#6e6e6e;
  --line:#d8d8d8;
  --white:#ffffff;
  --footer:#2c2c2c;
  --footer-text:#bdbdbd;
}
*{box-sizing:border-box;margin:0;padding:0}
html,body{width:1200px;height:2507px;overflow:hidden}
body{position:relative;font-family:"Figtree",Arial,sans-serif;color:var(--ink);background:var(--white)}
.abs{position:absolute}

/* header */
.site-header{left:0;top:0;width:1200px;height:79px;background:var(--white)}
.brand{left:159px;top:22px;height:36px;display:flex;align-items:center;gap:10px}
.brand-mark{width:26px;height:26px;background:var(--brand)}
.brand-name{font-size:19px;font-weight:700;color:var(--ink)}
.main-nav a{position:absolute;top:28px;font-size:14px;color:#555;text-decoration:none}
.phone-btn{left:990px;top:20px;width:34px;height:34px;border:2px solid var(--brand);border-radius:50%;display:flex;align-items:center;justify-content:center}

/* hero */
.hero{left:0;top:79px;width:1200px;height:526px;background:linear-gradient(120deg,#7a7670 0%,#9a948b 35%,#6e6a64 70%,#8a857c 100%)}
.hero-shade{left:0;top:79px;width:1200px;height:526px;background:rgba(30,30,30,.35)}
.hero-title{left:0;top:226px;width:1200px;text-align:center;font-size:40px;font-weight:500;color:var(--white)}
.hero-sub{left:0;top:291px;width:1200px;text-align:center;font-size:23px;color:var(--accent-yellow)}
.zip-panel{left:179px;top:356px;width:413px;height:87px;background:rgba(40,40,40,.75)}
.zip-input{left:202px;top:379px;width:238px;height:40px;background:var(--white);border:2px solid var(--brand);font-size:14px;color:var(--brand);padding:0 14px;line-height:36px}
.zip-button{left:440px;top:379px;width:133px;height:40px;background:var(--brand);color:var(--white);font-size:14px;text-align:center;line-height:40px}
.benefits{left:620px;top:349px;list-style:none}
.benefits li{height:24.5px;display:flex;align-items:center;gap:10px;font-size:11.5px;font-weight:700;color:var(--white)}

/* timer band */
.timer-band{left:0;top:605px;width:1200px;height:57px;background:var(--brand);color:var(--white);font-size:19px;display:flex;align-items:center;justify-content:center;gap:18px}
.timer{border:2px solid var(--white);width:66px;height:30px;line-height:26px;text-align:center;font-weight:700}

/* testimonial */
.quote-badge{left:571px;top:711px;width:42px;height:42px;border:2px solid #c9c9c9;border-radius:50%;color:#999;font-size:28px;text-align:center;line-height:48px;font-weight:700}
.testimonial-text{left:280px;top:787px;width:640px;text-align:center;font-size:13.5px;line-height:21px;color:var(--muted)}
.testimonial-by{left:0;top:864px;width:1200px;text-align:center;font-size:13.5px;color:var(--ink)}
.testimonial-by em{color:var(--brand);font-weight:600}
.slider-arrow{top:796px}
.slider-dots{left:565px;top:931px;display:flex;gap:3px}
.slider-dots span{width:10px;height:10px;border-radius:50%;background:var(--brand)}
.slider-dots span.off{background:transparent;border:1.5px solid var(--brand)}

/* calculator band */
.calc-band{left:0;top:1003px;width:1200px;height:294px;background:linear-gradient(180deg,#3e3e3e 0%,#6a6a6a 60%,#4a4a4a 100%)}
.calc-text{left:159px;top:1107px;width:420px;font-size:18px;line-height:27.5px;color:var(--white)}
.calc-button{left:693px;top:1116px;width:171px;height:42px;border:2px solid var(--brand);color:var(--brand);font-size:11.5px;letter-spacing:1.6px;text-align:center;line-height:38px;font-weight:600}

/* steps */
.step-icon{width:146px;height:146px;border-radius:50%;border:2px solid #dcdcdc;background:radial-gradient(circle,#f6f6f6 0%,#e9e9e9 100%)}
.step-title{font-size:22px;font-weight:700;color:var(--brand);letter-spacing:.5px}
.step-rule{height:1px;width:70px;background:var(--line)}
.step-text{font-size:11.5px;line-height:22px;color:var(--muted);width:360px}
.right{text-align:right}

/* about */
.about{left:0;top:2032px;width:1200px;height:344px;background:var(--brand)}
.about-title{left:159px;top:2092px;font-size:27px;font-weight:500;color:var(--white)}
.about-text{left:159px;top:2143px;width:370px;font-size:11.5px;line-height:22px;color:var(--white)}
.video{left:592px;top:2099px;width:432px;height:220px;background:linear-gradient(120deg,#4b3b33 0%,#8b7d70 45%,#c4b9ab 60%,#5a4e46 100%)}
.play{left:792px;top:2186px;width:60px;height:60px;border:2px solid var(--white);border-radius:50%}

/* footer */
.site-footer{left:0;top:2376px;width:1200px;height:131px;background:var(--footer)}
.footer-nav{left:0;top:2416px;width:1200px;display:flex;justify-content:center;gap:0;font-size:11px;color:var(--white)}
.footer-nav span{padding:0 22px}
.footer-nav .sep{padding:0;color:#888}
.copyright{left:0;top:2450px;width:1200px;text-align:center;font-size:10px;color:var(--footer-text)}
</style>
</head>
<body>

<header class="site-header abs">
  <div class="brand abs"><span class="brand-mark"></span><span class="brand-name">Blue Harbor Car Finance</span></div>
  <nav class="main-nav">
    <a style="left:560px">Locations</a>
    <a style="left:660px">Finance Center</a>
    <a style="left:779px">About</a>
    <a style="left:849px">FAQs</a>
    <a style="left:914px">Contact</a>
  </nav>
  <div class="phone-btn abs">
    <svg width="16" height="16" viewBox="0 0 24 24"><path d="M6.6 10.8a15.1 15.1 0 0 0 6.6 6.6l2.2-2.2a1 1 0 0 1 1-.25 11.4 11.4 0 0 0 3.6.57 1 1 0 0 1 1 1V20a1 1 0 0 1-1 1A17 17 0 0 1 3 4a1 1 0 0 1 1-1h3.5a1 1 0 0 1 1 1c0 1.25.2 2.45.57 3.57a1 1 0 0 1-.25 1z" fill="#9bcb3b"/></svg>
  </div>
</header>

<section>
  <div class="hero abs" role="img" aria-label="Photo of two smiling people reviewing loan paperwork at an office desk"></div>
  <div class="hero-shade abs"></div>
  <h1 class="hero-title abs">Over 30,000 Auto Loans Since 2000</h1>
  <p class="hero-sub abs">Pre Approval in Under 60 Seconds!</p>
  <div class="zip-panel abs"></div>
  <div class="zip-input abs">Enter Zip Code</div>
  <div class="zip-button abs">Get Approved</div>
  <ul class="benefits abs">
    <li><svg width="14" height="12" viewBox="0 0 14 12"><path d="M1 6l4 4 8-9" stroke="#9bcb3b" stroke-width="2.4" fill="none"/></svg>No Social Security Number Required</li>
    <li><svg width="14" height="12" viewBox="0 0 14 12"><path d="M1 6l4 4 8-9" stroke="#9bcb3b" stroke-width="2.4" fill="none"/></svg>Instant Approval</li>
    <li><svg width="14" height="12" viewBox="0 0 14 12"><path d="M1 6l4 4 8-9" stroke="#9bcb3b" stroke-width="2.4" fill="none"/></svg>No Application Fees</li>
    <li><svg width="14" height="12" viewBox="0 0 14 12"><path d="M1 6l4 4 8-9" stroke="#9bcb3b" stroke-width="2.4" fill="none"/></svg>All Credit Accepted</li>
  </ul>
</section>

<div class="timer-band abs"><span>Apply within</span><span class="timer">3:00</span><span>and see your credit score for free!</span></div>

<section>
  <div class="quote-badge abs">&ldquo;</div>
  <svg class="slider-arrow abs" style="left:160px" width="14" height="28" viewBox="0 0 14 28"><path d="M12 2L2 14l10 12" stroke="#9bcb3b" stroke-width="2" fill="none"/></svg>
  <svg class="slider-arrow abs" style="left:1011px" width="14" height="28" viewBox="0 0 14 28"><path d="M2 2l10 12L2 26" stroke="#777" stroke-width="2" fill="none"/></svg>
  <p class="testimonial-text abs">Lorem Ipsum is simply dummy text of the printing and typesetting industry. Lorem Ipsum has been the industry's standard dummy text ever since the 1500s, when an unknown printer took a galley</p>
  <p class="testimonial-by abs">- Satisfied Customer, <em>Web Designer</em></p>
  <div class="slider-dots abs"><span class="off"></span><span></span><span></span><span></span></div>
</section>

<section>
  <div class="calc-band abs" role="img" aria-label="Dark photo of a laptop and documents on a desk"></div>
  <p class="calc-text abs">Lorem Ipsum is simply dummy text of the printing and typesetting industry. Lorem Ipsum has been the industry's standard</p>
  <div class="calc-button abs">CALCULATE PAYMENT</div>
</section>

<section>
  <div class="step-icon abs" style="left:158px;top:1381px" role="img" aria-label="Illustration of a document being signed with a pen"></div>
  <h2 class="step-title abs" style="left:334px;top:1378px">STEP 1</h2>
  <div class="step-rule abs" style="left:334px;top:1417px"></div>
  <p class="step-text abs" style="left:334px;top:1431px">Lorem Ipsum is simply dummy text of the printing and typesetting industry. Lorem Ipsum has been the industry's standard dummy text ever since the 1500s, when an unknown printer took a galley of type and scrambled it to make a type specimen book.</p>

  <div class="step-icon abs" style="left:876px;top:1593px" role="img" aria-label="Illustration of a green car with a magnifying glass"></div>
  <h2 class="step-title abs right" style="left:700px;top:1590px;width:149px">STEP 2</h2>
  <div class="step-rule abs" style="left:779px;top:1629px"></div>
  <p class="step-text abs right" style="left:492px;top:1643px">Lorem Ipsum is simply dummy text of the printing and typesetting industry. Lorem Ipsum has been the industry's standard dummy text ever since the 1500s, when an unknown printer took a galley of type and scrambled it to make a type specimen book.</p>

  <div class="step-icon abs" style="left:159px;top:1809px" role="img" aria-label="Illustration of two hands shaking"></div>
  <h2 class="step-title abs" style="left:334px;top:1804px">STEP 3</h2>
  <div class="step-rule abs" style="left:334px;top:1843px"></div>
  <p class="step-text abs" style="left:334px;top:1855px">Lorem Ipsum is simply dummy text of the printing and typesetting industry. Lorem Ipsum has been the industry's standard dummy text ever since the 1500s, when an unknown printer took a galley of type and scrambled it to make a type specimen book.</p>
</section>

<section>
  <div class="about abs"></div>
  <h2 class="about-title abs">Blue Harbor Car Finance</h2>
  <p class="about-text abs">Lorem Ipsum is simply dummy text of the printing and typesetting industry. Lorem Ipsum has been the industry's standard dummy text ever since the 1500s, when an unknown printer took a galley of type and scrambled it to make a type specimen book.</p>
  <div class="video abs" role="img" aria-label="Video still of a smiling woman using a tablet in a cafe"></div>
  <div class="play abs"><svg width="56" height="56" viewBox="0 0 56 56"><path d="M23 18l14 10-14 10z" fill="#ffffff"/></svg></div>
</section>

<footer class="site-footer abs">
  <div class="footer-nav abs"><span>HOME</span><span class="sep">|</span><span>ABOUT</span><span class="sep">|</span><span>PRIVACY</span><span class="sep">|</span><span>CONTACT</span></div>
  <p class="copyright abs">© 2016 Blue Harbor Car Finance. All Right Reserved.</p>
</footer>

</body>
</html>
```